PowerPoint Corporate Template for Healthcare AI Technology Company

Take logo and create a comprehensive source file for corporate PowerPoint presentation library that provides an array of title/separator slides, graphic presentation options, chart options and text slide options. Utilize the current logo files and provide options on white backgrounds, and knock out options.

Target Market(s)

Pharmaceutical Manufacturers

Font styles to use
Sans Serif

Colors
6b449b
0556a4
33a6d7
0393ce
ffffff
e34197

Requirements
Must have
• Use logos upgraded in files; create an embedded color palette that aligns to the logo; include multiple options for different types of slides including charts; create a bullet point that is the logo in the purple/blue color with white background; incorporate knock out logo version option for separator pages; must include page numbers; use font aligned to logo for text slide options
Nice to have
• Tech looking, data intensive slide options that communicate easily; could be using 3-4 data points per slide
Should not have
• Any logo other than what has been shared

```html
<!DOCTYPE html>
<html lang="en">
<head>
<meta charset="UTF-8">
<title>Title Slide</title>
<link href="https://fonts.googleapis.com/css2?family=Montserrat:wght@200;300;500;600&family=Inter:wght@300;700&display=swap" rel="stylesheet">
<style>
  :root {
    --slide-bg: #1b1c1e;
    --brand-violet: #6670b6;
    --text-white: #ffffff;
    --text-soft: #e6e6e8;
  }
  html, body {
    margin: 0;
    padding: 0;
    width: 1200px;
    height: 674px;
    overflow: hidden;
    background: var(--slide-bg);
  }
  .slide {
    position: relative;
    width: 1200px;
    height: 674px;
    background: var(--slide-bg);
    color: var(--text-white);
  }
  .brand {
    position: absolute;
    top: 142px;
    left: 0;
    width: 100%;
    display: flex;
    justify-content: center;
    align-items: center;
    gap: 16px;
  }
  .brand-dot {
    width: 78px;
    height: 78px;
    border-radius: 50%;
    border: 2px solid var(--brand-violet);
    box-sizing: border-box;
  }
  .brand-name {
    font-family: "Montserrat", sans-serif;
    font-weight: 200;
    font-size: 60px;
    line-height: 1;
    color: var(--brand-violet);
  }
  .title-block {
    position: absolute;
    top: 310px;
    left: 0;
    width: 100%;
    text-align: center;
  }
  .slide-title {
    margin: 0;
    font-family: "Montserrat", sans-serif;
    font-weight: 600;
    font-size: 44px;
    line-height: 60px;
    letter-spacing: -0.3px;
    color: var(--text-white);
  }
  .slide-subtitle {
    margin: 6px 0 0;
    font-family: "Inter", sans-serif;
    font-weight: 300;
    font-size: 17px;
    letter-spacing: 6px;
    color: var(--text-soft);
  }
  .presenter {
    position: absolute;
    top: 510px;
    left: 0;
    width: 100%;
    text-align: center;
  }
  .presenter-label {
    margin: 0;
    font-family: "Inter", sans-serif;
    font-weight: 300;
    font-size: 17px;
    letter-spacing: 5.5px;
    color: var(--text-soft);
  }
  .presenter-name {
    margin: 2px 0 0;
    font-family: "Inter", sans-serif;
    font-weight: 700;
    font-size: 16px;
    color: var(--text-white);
  }
</style>
</head>
<body>
  <main class="slide">
    <div class="brand">
      <span class="brand-dot" aria-hidden="true"></span>
      <span class="brand-name">Corvella</span>
    </div>
    <header class="title-block">
      <h1 class="slide-title">Prestation Title Goes Here</h1>
      <p class="slide-subtitle">SUB TITLE GOES HERE</p>
    </header>
    <section class="presenter">
      <p class="presenter-label">PRESENTED BY</p>
      <p class="presenter-name">Presenter name</p>
    </section>
  </main>
</body>
</html>
```